Stonewell Holdings

Professional looking business card using darker colours
I do not yet have a logo for the company so feel free to suggest
The business is based on consultancy and project management
Based in Melbourne
Business card can omit the word "Holdings" and can be Stonewell consulting etc.

Contact Name on card : Ravi Pelunkoda Contact number : +61433 512 604 Email address will be confirmed shortly.

```html
<!DOCTYPE html>
<html lang="en">
<head>
<meta charset="utf-8">
<title>Stonewell Consulting – Business Card</title>
<link href="https://fonts.googleapis.com/css2?family=Italianno&family=PT+Sans:wght@400;700&display=swap" rel="stylesheet">
<style>
  :root {
    --page-bg: #ffffff;
    --card-bg: #999999;
    --ink-dark: #333333;
    --ink-black: #000000;
    --ink-light: #ffffff;
    --accent-light: #c4c4c4;
    --band-dark: #4a4a4a;
    --band-light: #e5e5e5;
  }
  html, body {
    margin: 0;
    padding: 0;
    width: 1200px;
    height: 1000px;
    overflow: hidden;
    background: var(--page-bg);
  }
  .canvas {
    position: relative;
    width: 1200px;
    height: 1000px;
  }
  .business-card {
    position: absolute;
    left: 365px;
    top: 247px;
    width: 682px;
    height: 383px;
    background: var(--card-bg);
    overflow: hidden;
  }
  .card-art {
    position: absolute;
    left: 0;
    top: 0;
    width: 682px;
    height: 383px;
  }
  .logo-placeholder {
    position: absolute;
    left: 37px;
    top: 26px;
    width: 61px;
    height: 61px;
    border-radius: 50%;
    background: var(--ink-black);
  }
  .ornament-placeholder {
    position: absolute;
    height: 14px;
  }
  .ornament-top {
    left: 180px;
    top: 124px;
    width: 153px;
    background: var(--ink-dark);
  }
  .ornament-bottom {
    left: 425px;
    top: 205px;
    width: 154px;
    background: var(--accent-light);
  }
  .contact-name {
    position: absolute;
    left: 116px;
    top: 28px;
    margin: 0;
    font-family: "Italianno", cursive;
    font-weight: 400;
    font-size: 58px;
    line-height: 60px;
    white-space: nowrap;
    color: var(--ink-light);
  }
  .company-name {
    position: absolute;
    left: 176px;
    top: 140px;
    margin: 0;
    font-family: "PT Sans", sans-serif;
    font-weight: 700;
    font-size: 45.5px;
    line-height: 56px;
    letter-spacing: -0.2px;
    white-space: nowrap;
    color: var(--ink-dark);
  }
  .contact-list {
    position: absolute;
    left: 37px;
    top: 247px;
    margin: 0;
    padding: 0;
    list-style: none;
    font-family: "PT Sans", sans-serif;
    font-size: 24.5px;
    line-height: 37px;
    white-space: nowrap;
    color: var(--ink-light);
  }
</style>
</head>
<body>
<main class="canvas">
  <section class="business-card" aria-label="Stonewell Consulting business card">
    <svg class="card-art" viewBox="0 0 682 383" aria-hidden="true">
      <circle cx="17" cy="267" r="5.5" fill="var(--ink-light)" stroke="var(--ink-black)" stroke-width="3.5"/>
      <circle cx="19" cy="302" r="5.5" fill="var(--ink-light)" stroke="var(--ink-black)" stroke-width="3.5"/>
      <polygon class="band-dark" points="0,361 244,361 218,383 0,383" fill="var(--band-dark)"/>
      <polygon class="band-light" points="280,349 682,349 682,383 252,383" fill="var(--band-light)"/>
    </svg>
    <div class="logo-placeholder" role="img" aria-label="Logo mark area"></div>
    <div class="ornament-placeholder ornament-top" role="img" aria-label="Decorative arrow ornament pointing right"></div>
    <div class="ornament-placeholder ornament-bottom" role="img" aria-label="Decorative arrow ornament pointing left"></div>
    <h1 class="contact-name">Ravi Pelunkoda</h1>
    <h2 class="company-name">Stonewell Consulting</h2>
    <ul class="contact-list">
      <li class="contact-phone">Contact Number : +61433 512 604</li>
      <li class="contact-email">Email</li>
    </ul>
  </section>
</main>
</body>
</html>
```